Brightpath EAP 2 x Flyer with Poster

Brightpath is an award-winning organisation providing dynamic and creative ways for children, young people, adults and families to make positive change and achieve fulfilling lives.
We are launching into a new area of business and starting to offer organisations Employee Assistance Program (EAP). To launch this service we need 2 flyers and a poster:
- 1 x flyer for employers
- 1 x flyer for employees
- 1 x poster (A3) for employees to be displayed around the office.
For the flyers we are after an a4 colour double sided flyer in either a A4 tri-fold to DL format or A4 bi-fold to A5 format. We are looking for a design that is simple and dynamic whilst keeping in line with our branding.
The winning designs will need to be hi-res and ready for print and also a lower res version suitable to email.
I have attached a number of files to provide further background, including:
• I have attached 3 x word doc of copy for each (2 x flyer / 1 x poster)
• Brand Guidelines
• Logo
• Our clinic flyer recently produced by a ArtHive designer for our clinic area of the business. These flyers do not have to be exactly the same as this one but should appear to be from the same organisation although a different service.
Generally we like our designs to be clear and simple.
Please don't hesitate to reach out with any Q's.

```html
<!DOCTYPE html>
<html lang="en">
<head>
<meta charset="utf-8">
<title>Brightpath EAP Booklet</title>
<link href="https://fonts.googleapis.com/css2?family=Poppins:wght@400;500;600;700;800&display=swap" rel="stylesheet">
<style>
:root{
  --bg:#e4e4e6;
  --paper:#ffffff;
  --ink:#3b3c3f;
  --dark:#2f3033;
  --green:#5f8a6a;
  --green-soft:#7aa083;
  --teal:#8fa9b0;
  --peach:#d8b59f;
  --grey-panel:#eef0f1;
  --text:#4a4b4e;
}
*{box-sizing:border-box;margin:0;padding:0}
html,body{width:1200px;height:2655px;overflow:hidden}
body{background:var(--bg);font-family:'Poppins',sans-serif;color:var(--text);position:relative}
.sheet{position:absolute;overflow:hidden;background:var(--paper);box-shadow:0 6px 18px rgba(0,0,0,.12)}
.abs{position:absolute}

/* ---------- front cover ---------- */
.cover{width:600px;height:850px;transform-origin:0 0}
.cover-corner{right:0;top:0}
.brand{display:flex;align-items:center;gap:12px;font-weight:600;color:var(--ink);white-space:nowrap}
.brand-dot{width:30px;height:30px;border-radius:50%;background:var(--green)}
.cover .brand{left:48px;top:52px;font-size:44px}
.cover-photo{left:150px;top:120px;width:450px;height:410px;background:linear-gradient(160deg,#f4f5f6 0%,#c9ccd0 35%,#8a7468 62%,#eef0f2 100%);
  -webkit-mask:linear-gradient(180deg,#000 75%,transparent 100%);mask:linear-gradient(180deg,#000 75%,transparent 100%)}
.cover-title{right:48px;top:500px;text-align:right;font-weight:800;font-size:35px;line-height:1.08;color:var(--ink);letter-spacing:.3px}
.cover-sub{right:48px;top:590px;text-align:right;font-size:21px;line-height:1.25;color:var(--ink)}
.cover-band{left:0;top:660px}
.cover-url{right:48px;top:683px;color:#fff;font-size:15px;letter-spacing:5px;font-weight:500}

/* ---------- back cover ---------- */
.back{background:var(--green)}
.back .brand{color:#fff;font-size:30px;left:36px;top:600px;gap:10px}
.back .brand-dot{background:#fff;width:22px;height:22px}
.back-url{left:36px;top:648px;color:#fff;font-size:12px;letter-spacing:2px;white-space:nowrap}
.back-divider{left:268px;top:570px;width:2px;height:120px;background:rgba(255,255,255,.45)}
.contacts{left:288px;top:570px;width:228px;list-style:none;color:#fff;font-size:13px;line-height:1.35}
.contacts li{display:flex;gap:10px;align-items:flex-start;margin-bottom:12px}
.icon{flex:0 0 22px;width:22px;height:22px;border-radius:50%;background:var(--peach);display:flex;align-items:center;justify-content:center}

/* ---------- inner spread ---------- */
.page-text{font-size:10px;line-height:1.5;color:var(--text)}
.label{display:inline-block;background:var(--green);color:#fff;font-weight:600;font-size:13px;padding:4px 14px}
.label strong{color:#fff}
.heading-dark{color:var(--ink);font-weight:600;font-size:17px}
.heading-dark b{color:var(--green)}
.dark-band{background:var(--dark);color:#d9dadc}
.dark-band .page-text{color:#d9dadc}
.why-box{background:var(--green);color:#fff}
.why-box .page-text{color:#eef3ef}
.pill{display:inline-flex;align-items:center;gap:8px;background:#fff;border-radius:14px;padding:3px 12px;font-size:11px;font-weight:600;color:var(--green)}
.num{display:inline-flex;align-items:center;justify-content:center;width:26px;height:20px;border-radius:10px;background:var(--peach);color:#fff;font-size:10px;font-weight:700;margin-right:8px}
.list{list-style:none;font-size:10px;line-height:1.6}
.list li::before{content:"› ";color:var(--peach);font-weight:700}
.small-url{font-size:11px;letter-spacing:4px;white-space:nowrap}
</style>
</head>
<body>

<!-- Row 1: front cover -->
<section class="sheet cover" style="left:300px;top:30px">
  <svg class="abs cover-corner" width="170" height="240" viewBox="0 0 170 240"><polygon points="60,0 170,0 170,240" fill="var(--dark)"/></svg>
  <div class="abs brand"><span class="brand-dot"></span>Brightpath</div>
  <div class="abs cover-photo" role="img" aria-label="Photo of a counsellor taking notes while a distressed man sits on a sofa"></div>
  <h1 class="abs cover-title">EMPLOYEE ASSISTANCE<br>PROGRAM (EAP)</h1>
  <p class="abs cover-sub">Counselling for Work Related<br>or Personal Issues</p>
  <svg class="abs cover-band" width="600" height="190" viewBox="0 0 600 190">
    <polygon points="120,0 600,0 600,45 90,45" fill="var(--teal)"/>
    <polygon points="105,160 600,160 600,190 100,190" fill="var(--teal)"/>
  </svg>
  <svg class="abs" style="left:0;top:420px" width="260" height="430" viewBox="0 0 260 430"><polygon points="0,80 160,270 95,430 0,430" fill="var(--green)"/></svg>
  <div class="abs cover-url">www.brightpath.example</div>
</section>

<!-- Row 2: back and front cover -->
<section class="sheet back" style="left:65px;top:920px;width:530px;height:750px">
  <svg class="abs" style="left:0;top:0" width="530" height="750" viewBox="0 0 530 750">
    <polygon points="330,0 530,0 530,16 330,16" fill="var(--peach)"/>
    <polygon points="0,640 0,750 80,750" fill="var(--dark)"/>
  </svg>
  <div class="abs back-divider"></div>
  <ul class="abs contacts">
    <li><span class="icon"><svg width="11" height="11" viewBox="0 0 24 24"><path d="M6.6 10.8a15 15 0 0 0 6.6 6.6l2.2-2.2a1 1 0 0 1 1-.25 11.4 11.4 0 0 0 3.6.57 1 1 0 0 1 1 1V20a1 1 0 0 1-1 1A17 17 0 0 1 3 4a1 1 0 0 1 1-1h3.5a1 1 0 0 1 1 1c0 1.25.2 2.45.57 3.57a1 1 0 0 1-.25 1z" fill="#fff"/></svg></span>(03) 9000 4821</li>
    <li><span class="icon"><svg width="11" height="11" viewBox="0 0 24 24"><path d="M12 2a7 7 0 0 0-7 7c0 5.25 7 13 7 13s7-7.75 7-13a7 7 0 0 0-7-7zm0 9.5A2.5 2.5 0 1 1 12 6.5a2.5 2.5 0 0 1 0 5z" fill="#fff"/></svg></span><span>Riverside Building<br>42 Elmwood Ave, Northvale VIC 3999</span></li>
    <li><span class="icon"><svg width="11" height="11" viewBox="0 0 24 24"><path d="M3 5h18v14H3z M3 5l9 7 9-7" fill="none" stroke="#fff" stroke-width="2"/></svg></span>clinic@brightpath.example</li>
  </ul>
  <div class="abs brand"><span class="brand-dot"></span>Brightpath</div>
  <div class="abs back-url">www.brightpath.example</div>
</section>
<section class="sheet cover" style="left:605px;top:920px;transform:scale(.8833)">
  <svg class="abs cover-corner" width="170" height="240" viewBox="0 0 170 240"><polygon points="60,0 170,0 170,240" fill="var(--dark)"/></svg>
  <div class="abs brand"><span class="brand-dot"></span>Brightpath</div>
  <div class="abs cover-photo" role="img" aria-label="Photo of a counsellor taking notes while a distressed man sits on a sofa"></div>
  <h2 class="abs cover-title">EMPLOYEE ASSISTANCE<br>PROGRAM (EAP)</h2>
  <p class="abs cover-sub">Counselling for Work Related<br>or Personal Issues</p>
  <svg class="abs cover-band" width="600" height="190" viewBox="0 0 600 190">
    <polygon points="120,0 600,0 600,45 90,45" fill="var(--teal)"/>
    <polygon points="105,160 600,160 600,190 100,190" fill="var(--teal)"/>
  </svg>
  <svg class="abs" style="left:0;top:420px" width="260" height="430" viewBox="0 0 260 430"><polygon points="0,80 160,270 95,430 0,430" fill="var(--green)"/></svg>
  <div class="abs cover-url">www.brightpath.example</div>
</section>

<!-- Row 3: inner spread -->
<section class="sheet" style="left:40px;top:1760px;width:1120px;height:800px">
  <!-- left page -->
  <svg class="abs" style="left:0;top:0" width="560" height="800" viewBox="0 0 560 800">
    <polygon points="0,0 560,0 560,230 0,330" fill="var(--dark)"/>
    <polygon points="0,770 560,770 560,800 0,800" fill="var(--dark)"/>
  </svg>
  <div class="abs dark-band" style="left:28px;top:26px;width:510px;background:none">
    <span class="label">How can <strong>Brightpath's</strong> EAP benefit you?</span>
    <div style="display:flex;gap:22px;margin-top:12px">
      <p class="page-text" style="flex:1">Brightpath's Employee Assistance Program (EAP) allows employers to support their staff and families through confidential counselling sessions with psychologists. The help offered lets employees manage personal issues that may affect workplace wellbeing, performance and productivity.<br><br>A large study found that EAP use was linked with improved work engagement and life satisfaction, and lower absenteeism and distress. These results support a focus on physical and emotional health.</p>
      <p class="page-text" style="flex:1">Access to an EAP provides a safe, confidential environment to understand and resolve issues that might impact their performance at work. Employees can gain coping skills and strategies, and the simple act of seeking help can improve morale.<br><br>An Employee Assistance Program is an employer funded, short-term professional help service for employees and their immediate families, covering personal and work issues that affect wellbeing and productivity.</p>
    </div>
  </div>
  <div class="abs" style="left:28px;top:350px;width:280px">
    <p class="heading-dark">Why Choose <b>Brightpath?</b></p>
    <p class="page-text" style="margin-top:8px">Brightpath is a registered provider with significant experience supporting children, young people, adults and families. Our team of psychologists and specialists work with clients across many settings, including schools, homes and the wider community, using a person-centred approach.<br><br>We provide tailored training and e-learning to individuals, families and service providers, and operate a clinic in Northvale.<br><br>We will develop a Service Agreement with you determining how many sessions you wish to provide your employees in a year. Sessions are only charged when used, so your staff have support available when they need it.<br><br>The Employee Assistance Program offers 50 minute consultations for the agreed number of sessions. Most employers offer 3–6 sessions per year.</p>
  </div>
  <div class="abs why-box" style="left:325px;top:300px;width:235px;height:460px;padding:20px 16px">
    <span class="label" style="background:#fff;color:var(--green)">Why Choose Brightpath?</span>
    <p class="page-text" style="margin-top:10px">Our highly skilled team provide short-term counselling and support for personal and work-related issues.</p>
    <p style="margin-top:12px;font-size:11px;font-weight:600"><span class="num">01</span>Our EAP program includes</p>
    <ul class="list" style="margin:6px 0 0 10px">
      <li>Employee Counselling</li><li>Mental Health Checks</li><li>Critical Incident Debriefing</li><li>Wellbeing Workshops</li><li>Career Coaching</li><li>Organisational Support</li>
    </ul>
    <p style="margin-top:12px;font-size:11px;font-weight:600"><span class="num">02</span>Brightpath offers your employees</p>
    <ul class="list" style="margin:6px 0 0 10px">
      <li>A highly confidential service</li><li>Experienced registered psychologists</li><li>Flexible appointment times</li><li>Face to face, telehealth or phone options</li>
    </ul>
    <p class="page-text" style="margin-top:10px">Our aim is to provide early-intervention, solution focused support so employees develop effective coping strategies and return to their best.</p>
  </div>
  <div class="abs small-url" style="left:28px;top:778px;color:#fff">www.brightpath.example</div>

  <!-- right page -->
  <div class="abs" style="left:560px;top:0;width:560px;height:800px;background:var(--grey-panel)"></div>
  <div class="abs" role="img" aria-label="Photo of two people holding hands in comfort" style="left:850px;top:0;width:270px;height:260px;background:linear-gradient(150deg,#cfc7cc,#b79a86 55%,#e7e3e6)"></div>
  <div class="abs" role="img" aria-label="Photo of a team stacking hands together" style="left:910px;top:300px;width:210px;height:400px;background:linear-gradient(200deg,#8ea7b5,#c9b7a6 50%,#dde3e6)"></div>
  <svg class="abs" style="left:560px;top:0" width="560" height="800" viewBox="0 0 560 800">
    <polygon points="0,320 330,260 345,300 330,720 0,720" fill="#fff"/>
    <polygon points="300,720 560,720 560,750 290,750" fill="var(--peach)"/>
  </svg>
  <div class="abs" style="left:590px;top:30px;width:245px">
    <span class="label">Appointment bookings</span>
    <ul class="list" style="margin-top:8px;color:var(--text)">
      <li>Employees can contact Brightpath directly to book appointments.</li>
      <li>The Employer can also directly refer employees for counselling.</li>
      <li>Brightpath will arrange an appointment time with the employee.</li>
    </ul>
    <span class="label" style="margin-top:12px">Session extensions</span>
    <ul class="list" style="margin-top:8px">
      <li>If further sessions are required, the employer representative will be contacted.</li>
      <li>Further sessions are allocated at the discretion of the Employer.</li>
      <li>If declined, further sessions may continue privately.</li>
    </ul>
  </div>
  <div class="abs" style="left:590px;top:340px;width:295px">
    <span class="label">Confidentiality</span>
    <p class="page-text" style="margin-top:8px">All employee personal information collected by Brightpath during counselling will remain confidential and secure except when:</p>
    <ul class="list" style="margin-top:4px">
      <li>It is subpoenaed by a court, or</li>
      <li>Failure to disclose would place a person at risk.</li>
      <li>The employee's prior consent has been obtained.</li>
    </ul>
    <p class="page-text" style="margin-top:6px">Confidentiality and its limits are explained to employees at the beginning of the counselling process.</p>
    <span class="label" style="margin-top:14px">Reporting</span>
    <p class="page-text" style="margin-top:8px">All sessions remain strictly confidential. Brightpath will provide statistical information to the employer on a quarterly basis including:</p>
    <ul class="list" style="margin-top:4px">
      <li>Number of employees that received services</li>
      <li>Total number of sessions provided</li>
      <li>Presenting issues and relevant trends</li>
    </ul>
    <p class="page-text" style="margin-top:8px">If you'd like to speak to us about EAP for your organisation, please contact us on</p>
    <span class="pill" style="margin-top:6px;background:var(--green);color:#fff">(03) 9000 4821</span>
  </div>
  <div class="abs small-url" style="left:890px;top:727px;color:#fff">www.brightpath.example</div>
</section>

</body>
</html>
```